Automotive component supplier needs a business card design

We need a business card design for our company called Velmar Global Components Ltd based in the UK. We are a supplier of interior and exterior components to premium car manufacturers such as Corvane Hale, Durrant Fyfe, Maxtorn and Valdessimo. We would like to see a modern business card design that uses the colour blue.

Target Market(s)

Premium automotive car manufacturers.

Industry/Entity Type

Automotive

Contact Information for Business Card

Company Name : Velmar Global Components Limited
Address: 17 Tamsey Yard, Upper Drisk, Warwick, CV31 8RJ, United Kingdom
Web Address : www.velmarparts-example.co.uk

Font styles to use
Other font styles liked:
• Helvetica

Colors
3176b5
0255a3
85acd3
cfdeed
cee9f5
85cae6
34a6d7
0692cd
9bcb3c

Requirements
Must have
• Clear company logo and a mixture of blue colours.
Nice to have
• A high quality modern image.
Should not have
• Multiple colours.

```html
<!DOCTYPE html>
<html lang="en">
<head>
<meta charset="utf-8">
<title>Velmar Global Components – Business Card</title>
<link href="https://fonts.googleapis.com/css2?family=Arimo:wght@400;700&display=swap" rel="stylesheet">
<style>
  :root {
    --blue-deep: #0255a3;
    --blue-mid: #3176b5;
    --blue-bright: #0692cd;
    --blue-sky: #34a6d7;
    --blue-soft: #85acd3;
    --green: #9bcb3c;
    --white: #ffffff;
    --stage: #e4e7ea;
  }
  * { margin: 0; padding: 0; box-sizing: border-box; }
  html, body { width: 1200px; height: 900px; overflow: hidden; }
  body {
    background: var(--stage);
    font-family: "Arimo", Helvetica, Arial, sans-serif;
    position: relative;
  }
  .card {
    position: absolute;
    top: 295px;
    width: 540px;
    height: 310px;
    border-radius: 22px;
    overflow: hidden;
    box-shadow: 0 10px 30px rgba(0,0,0,.18);
  }

  /* Front */
  .card-front { left: 40px; background: var(--white); }
  .brand {
    position: absolute;
    display: flex;
    align-items: center;
    gap: 10px;
  }
  .brand-mark { width: 12px; height: 12px; background: var(--green); }
  .brand-name {
    font-weight: 700;
    font-size: 25px;
    letter-spacing: 0.5px;
    color: var(--blue-bright);
    text-transform: uppercase;
  }
  .card-front .brand { left: 40px; top: 40px; }

  .person { position: absolute; left: 40px; top: 128px; }
  .person-name {
    font-weight: 700; font-size: 23px; color: var(--blue-bright);
    text-transform: uppercase; letter-spacing: 0.3px;
  }
  .person-role {
    font-weight: 700; font-size: 13px; color: var(--green);
    text-transform: uppercase; margin-top: 3px; letter-spacing: 0.3px;
  }

  .contact-divider {
    position: absolute; left: 248px; top: 166px;
    width: 1px; height: 86px; background: var(--blue-sky);
  }
  .contact-list {
    position: absolute; left: 264px; top: 166px; list-style: none;
  }
  .contact-item {
    display: flex; align-items: center; gap: 8px;
    height: 21px; font-size: 14px; color: var(--blue-deep);
  }
  .contact-item svg { width: 13px; height: 13px; flex: none; }

  .side-tab {
    position: absolute; right: 0; top: 148px;
    width: 30px; height: 44px; background: var(--blue-bright);
  }
  .address-band {
    position: absolute; left: 0; right: 0; bottom: 0; height: 38px;
    background: linear-gradient(90deg, var(--green) 0%, var(--blue-deep) 42%, var(--blue-mid) 75%, var(--blue-soft) 100%);
    display: flex; align-items: center; padding-left: 40px;
    color: var(--white); font-weight: 700; font-size: 13.5px;
  }

  /* Back */
  .card-back {
    left: 620px;
    background: linear-gradient(180deg, var(--blue-soft) 0%, var(--blue-deep) 30%, var(--blue-bright) 55%, var(--green) 100%);
  }
  .card-back .brand {
    left: 0; right: 0; top: 112px; justify-content: center;
  }
  .card-back .brand-name { color: var(--white); }
  .card-back .brand-mark { background: var(--white); }
  .back-web {
    position: absolute; left: 0; right: 0; bottom: 48px;
    text-align: center; color: var(--white);
    font-weight: 700; font-size: 15px; letter-spacing: 1.5px;
    text-transform: uppercase;
  }
</style>
</head>
<body>

  <section class="card card-front">
    <div class="brand">
      <span class="brand-mark"></span>
      <span class="brand-name">Velmar Global Components</span>
    </div>

    <div class="person">
      <div class="person-name">Martin Crewe</div>
      <div class="person-role">Managing Director</div>
    </div>

    <div class="contact-divider"></div>
    <ul class="contact-list">
      <li class="contact-item">
        <svg viewBox="0 0 14 14"><rect x="1.5" y="2.5" width="11" height="8" rx="1" fill="none" stroke="#9bcb3c" stroke-width="1.5"/><rect x="4.5" y="11.5" width="5" height="1.5" fill="#9bcb3c"/></svg>
        045 810 272
      </li>
      <li class="contact-item">
        <svg viewBox="0 0 14 14"><path d="M3 1.5l2.5 0 1 3-1.6 1.2a8 8 0 0 0 3.4 3.4L9.5 7.5l3 1v2.5c0 .8-.7 1.5-1.5 1.5A10 10 0 0 1 1.5 3c0-.8.7-1.5 1.5-1.5z" fill="#9bcb3c"/></svg>
        234 590 618
      </li>
      <li class="contact-item">
        <svg viewBox="0 0 14 14"><rect x="1" y="3" width="12" height="8.5" fill="#9bcb3c"/><path d="M1 3l6 5 6-5" fill="none" stroke="#fff" stroke-width="1.2"/></svg>
        info@velmarparts-example.co.uk
      </li>
      <li class="contact-item">
        <svg viewBox="0 0 14 14"><circle cx="7" cy="7" r="5.8" fill="none" stroke="#9bcb3c" stroke-width="1.3"/><ellipse cx="7" cy="7" rx="2.5" ry="5.8" fill="none" stroke="#9bcb3c" stroke-width="1.1"/><path d="M1.2 7h11.6M2.2 4h9.6M2.2 10h9.6" stroke="#9bcb3c" stroke-width="1"/></svg>
        www.velmarparts-example.co.uk
      </li>
    </ul>

    <div class="side-tab"></div>
    <div class="address-band">17 Tamsey Yard, Upper Drisk, Warwick, CV31 8RJ, United Kingdom</div>
  </section>

  <section class="card card-back">
    <div class="brand">
      <span class="brand-mark"></span>
      <span class="brand-name">Velmar Global Components</span>
    </div>
    <div class="back-web">www.velmarparts-example.co.uk</div>
  </section>

</body>
</html>
```